Pitch Deck presentation

Design multiple graphics and slides that can be used in a PowerPoint presentation.
4 infographics, text templates and blank templates
Attached you will find the infographics references and a couple of styles we would like to have on the presentations
We prefer a simpler design with not too much background noise or colors(prefer to have whiter backgrounds)
The infographics in the whiteboard should be presented 1 per slide with space on the right side to write text for explanation.
4 total columns will be the equivalent to the 4 different slides with design in the presentation.
Attached you have our colors and logos.
https://files.plenvora.net/share/7kqTw2mBx9RfL4pZ
You can reach out to me with any questions at my email mtressall@haulvenix.com
Look and feel
Each slider illustrates characteristics of the customer's brand and the style your logo design should communicate.

```html
<!DOCTYPE html>
<html lang="en">
<head>
<meta charset="utf-8">
<title>Haulway Infographic Deck – Slide Overview</title>
<link href="https://fonts.googleapis.com/css2?family=Poppins:wght@400;500;600;700&display=swap" rel="stylesheet">
<style>
:root{
  --bg:#f5f1ee;
  --or:#f0521e;
  --or-d:#c8401a;
  --ink:#1d1d1d;
  --mute:#8a8a8a;
  --line:#e3e3e3;
  --dark:#1f1f1f;
  --card:#ffffff;
}
*{margin:0;padding:0;box-sizing:border-box}
html,body{width:1200px;height:866px;overflow:hidden;background:var(--bg);font-family:'Poppins',sans-serif;color:var(--ink)}
.deck{position:absolute;left:38px;top:36px;display:grid;grid-template-columns:repeat(6,167px);column-gap:22.4px;grid-auto-rows:94px;row-gap:21.3px}
.slide{position:relative;background:#fff;overflow:hidden;box-shadow:0 3px 8px rgba(0,0,0,.06)}
.slide.dark{background:var(--dark);color:#fff}
.abs{position:absolute}
.brand{font-weight:700;letter-spacing:.2px;color:var(--ink)}
.dark .brand,.foot .brand{color:#fff}
.mini-brand{position:absolute;left:3px;top:3px;font-size:3px;font-weight:700}
.t{position:absolute;left:0;right:0;top:8px;text-align:center;font-size:5.6px;font-weight:500}
.t b{font-weight:600}
.t em,.or{color:var(--or);font-style:normal}
.p{font-size:2.1px;line-height:1.35;color:var(--mute)}
.foot{position:absolute;left:0;right:0;bottom:0;height:6.5px;background:var(--or);display:flex;justify-content:space-between;align-items:center;padding:0 4px;font-size:1.9px;color:#fff}
.foot .brand{font-size:3.2px}
.ph{position:absolute;border-radius:1px}
.ph.truck{background:linear-gradient(160deg,#e9e9ea 0%,#cfd1d4 55%,#7d8084 100%)}
.ph.road{background:linear-gradient(160deg,#8fb1cc 0%,#c4a676 55%,#56524c 100%)}
.ph.night{background:linear-gradient(160deg,#1c2a3a 0%,#30445a 60%,#12171e 100%)}
.ph.darkscene{background:linear-gradient(180deg,#2b2b2b 0%,#3a3530 60%,#1a1a1a 100%)}
.ph.face{background:linear-gradient(160deg,#d9c2ad,#8a7565);border-radius:50%}
.card{position:absolute;background:#fff;box-shadow:0 1px 3px rgba(0,0,0,.12);border-radius:1px}
.obox{position:absolute;background:var(--or);color:#fff;border-radius:1px}
.obox .p{color:#fff}
.icons{position:absolute;left:12px;right:12px;top:12px;display:grid;gap:5px 0;justify-items:center}
.ic{width:4px;height:4px;border:.6px solid var(--ink);border-radius:1px}
.ic.f{background:var(--ink)}
.ic.o{border-color:var(--or);border-radius:50%}
.rowline{display:flex;justify-content:space-between;border-bottom:.4px solid var(--line);font-size:2px;padding:1px 0;color:#444}
</style>
</head>
<body>
<main class="deck">

<!-- Row 1 -->
<section class="slide">
  <div class="abs brand" style="left:0;right:0;top:24px;text-align:center;font-size:5px">HAULWAY</div>
  <div class="abs" style="left:0;right:0;top:40px;text-align:center;font-size:9px;font-weight:700">Infographic Deck</div>
  <div class="abs or" style="left:0;right:0;top:55px;text-align:center;font-size:2.4px">Logistic Presentation Template</div>
  <div class="ph truck" role="img" aria-label="White semi truck with trailer" style="left:105px;top:56px;width:62px;height:38px"></div>
</section>

<section class="slide">
  <div class="abs" style="left:98px;top:0;width:46px;height:94px;background:var(--or)"></div>
  <div class="abs" style="left:10px;top:40px;font-size:7.5px;font-weight:700">Infographic Deck</div>
  <div class="abs or" style="left:10px;top:52px;font-size:2.4px">Logistic Presentation Template</div>
  <div class="ph truck" role="img" aria-label="White semi truck with branded trailer" style="left:85px;top:26px;width:82px;height:52px"></div>
  <div class="abs brand" style="left:126px;top:40px;font-size:6px">HAULWAY</div>
</section>

<section class="slide">
  <div class="mini-brand">HAULWAY</div>
  <div class="t" style="top:9px;font-weight:600">HWY Technology</div>
  <div class="abs" style="left:12px;top:23px;width:36px;font-size:2.3px;text-align:center">Budgeting Sustainable Rate</div>
  <div class="abs" style="left:12px;top:33px;width:36px;height:.5px;background:var(--or)"></div>
  <div class="abs p" style="left:14px;top:36px">Building Relationships</div>
  <div class="abs" style="left:12px;top:42px;width:36px;font-size:1.9px;font-weight:600;line-height:5.4px">
    <div>▸ 4 &nbsp;COMPETING</div><div>▸ 3 &nbsp;INCENTIVIZING</div><div>▸ 2 &nbsp;DIRECT CARRIER</div><div>▸ 1 &nbsp;TRANSPARENCY</div>
  </div>
  <svg class="abs" viewBox="0 0 167 94" style="left:0;top:0;width:167px;height:94px">
    <g stroke="var(--or)" stroke-width="1.4">
      <line x1="83" y1="57" x2="83" y2="40"/><line x1="83" y1="57" x2="64" y2="57"/><line x1="83" y1="57" x2="102" y2="57"/>
      <line x1="83" y1="57" x2="70" y2="71"/><line x1="83" y1="57" x2="96" y2="71"/><line x1="83" y1="57" x2="70" y2="44"/><line x1="83" y1="57" x2="96" y2="44"/><line x1="83" y1="57" x2="83" y2="76"/>
    </g>
    <g fill="var(--or)">
      <rect x="78" y="26" width="10" height="10" rx="1"/>
      <circle cx="83" cy="57" r="11"/>
      <circle cx="64" cy="57" r="4"/><circle cx="102" cy="57" r="4"/><circle cx="70" cy="71" r="4"/><circle cx="96" cy="71" r="4"/>
      <circle cx="70" cy="44" r="4"/><circle cx="96" cy="44" r="4"/><circle cx="83" cy="77" r="4"/>
    </g>
    <text x="83" y="56" fill="#fff" font-size="2.6" font-weight="700" text-anchor="middle">HWY</text>
    <text x="83" y="60" fill="#fff" font-size="2.6" font-weight="700" text-anchor="middle">Technology</text>
    <g font-size="1.8" fill="#555"><text x="102" y="30">→ 3 PER WEEK</text><text x="102" y="42">ESTABLISHED RATE</text><text x="102" y="84">CARRIER ROTATION</text></g>
  </svg>
  <div class="obox" style="left:120px;top:24px;width:39px;height:20px;padding:2px">
    <div style="font-size:2.2px;font-weight:600">Explanation One :</div>
    <div class="p">Short note on rate budgeting and weekly volume for steady pricing.</div>
  </div>
  <div class="abs" style="left:120px;top:47px;width:39px">
    <div style="font-size:2.2px;font-weight:600">Explanation Two :</div>
    <div class="p">Carrier rotation keeps capacity open and builds trust with partners over time.</div>
  </div>
</section>

<section class="slide">
  <div class="mini-brand">HAULWAY</div>
  <div class="t" style="top:8px;font-weight:600">SPOT Market</div>
  <div class="abs" style="left:0;right:0;top:16px;text-align:center;font-size:2.2px;color:#444">BROKERAGE MANAGED</div>
  <svg class="abs" viewBox="0 0 167 94" style="left:0;top:0;width:167px;height:94px">
    <rect x="20" y="24" width="14" height="5" fill="var(--or)"/><text x="27" y="27.5" fill="#fff" font-size="1.8" text-anchor="middle">SHIPPER</text>
    <rect x="22" y="33" width="10" height="10" fill="var(--or)"/>
    <line x1="34" y1="38" x2="58" y2="38" stroke="#999" stroke-width=".4"/><text x="59" y="39" font-size="1.8" fill="#555">1 SHIPMENT</text>
    <text x="27" y="50" font-size="1.8" text-anchor="middle">BROKERS</text>
    <g fill="var(--or)"><rect x="10" y="52" width="4" height="4"/><rect x="16" y="52" width="4" height="4"/><rect x="22" y="52" width="4" height="4"/><rect x="28" y="52" width="4" height="4"/><rect x="34" y="52" width="4" height="4"/><rect x="40" y="52" width="4" height="4"/>
    <rect x="17" y="62" width="4" height="4"/><rect x="25" y="62" width="4" height="4"/><rect x="33" y="62" width="4" height="4"/></g>
    <text x="27" y="71" font-size="1.8" text-anchor="middle">CARRIERS</text>
    <g font-size="1.8" fill="#555"><text x="59" y="55">→ DEMAND</text><text x="59" y="65">→ SUPPLY</text></g>
    <polyline points="80,48 83,44 86,46 89,40" fill="none" stroke="var(--or)" stroke-width=".7"/>
  </svg>
  <div class="obox" style="left:98px;top:23px;width:61px;height:64px;padding:3px">
    <div style="font-size:2.4px;font-weight:600;margin-bottom:1px">Explanation :</div>
    <div class="p">Spot freight moves through brokers who match shippers and carriers for each single load at the daily market price.</div>
    <div class="p" style="margin-top:2px">Rates shift with demand and supply, so planning early keeps costs stable across busy seasons.</div>
    <div class="p" style="margin-top:2px">Brokers add reach and flexibility while carriers keep full loads.</div>
  </div>
</section>

<section class="slide">
  <div class="mini-brand">HAULWAY</div>
  <div class="t" style="top:8px;font-weight:600">SPOT Market</div>
  <div class="abs" style="left:0;right:0;top:16px;text-align:center;font-size:2.2px;color:#444">HWY SHIPPER MANAGED</div>
  <svg class="abs" viewBox="0 0 167 94" style="left:0;top:0;width:167px;height:94px">
    <rect x="20" y="24" width="14" height="5" fill="var(--or)"/><text x="27" y="27.5" fill="#fff" font-size="1.8" text-anchor="middle">SHIPPER</text>
    <rect x="21" y="35" width="12" height="12" fill="var(--or)"/>
    <line x1="34" y1="41" x2="58" y2="41" stroke="#999" stroke-width=".4"/><text x="59" y="42" font-size="1.8" fill="#555">1 SHIPMENT</text>
    <g fill="var(--or)"><rect x="17" y="62" width="4" height="4"/><rect x="25" y="62" width="4" height="4"/><rect x="33" y="62" width="4" height="4"/></g>
    <text x="27" y="71" font-size="1.8" text-anchor="middle">CARRIERS</text>
    <text x="59" y="65" font-size="1.8" fill="#555">→ SUPPLY</text>
    <polyline points="80,42 83,38 86,40 89,44" fill="none" stroke="#5ab4e0" stroke-width=".7"/>
  </svg>
  <div class="obox" style="left:98px;top:23px;width:61px;height:64px;padding:3px">
    <div style="font-size:2.4px;font-weight:600;margin-bottom:1px">Explanation :</div>
    <div class="p">The shipper books carriers directly through one managed desk, removing extra layers and keeping full control of each load.</div>
    <div class="p" style="margin-top:2px">Fewer hand offs mean clearer tracking and faster answers for every shipment.</div>
    <div class="p" style="margin-top:2px">Carrier supply stays steady year round.</div>
  </div>
</section>

<section class="slide">
  <div class="mini-brand">HAULWAY</div>
  <div class="t" style="top:8px;font-weight:600">Traditional TMS</div>
  <svg class="abs" viewBox="0 0 167 94" style="left:0;top:0;width:167px;height:94px">
    <rect x="16" y="23" width="22" height="7" fill="var(--or)"/><text x="27" y="26" fill="#fff" font-size="1.7" text-anchor="middle">90% +</text><text x="27" y="28.5" fill="#fff" font-size="1.7" text-anchor="middle">ACCEPTANCE</text>
    <rect x="70" y="23" width="22" height="7" fill="var(--or)"/><text x="81" y="26" fill="#fff" font-size="1.7" text-anchor="middle">TRADITIONAL</text><text x="81" y="28.5" fill="#fff" font-size="1.7" text-anchor="middle">WAY</text>
    <g fill="#fff" stroke="#e5e5e5" stroke-width=".4">
      <rect x="36" y="34" width="22" height="6"/><rect x="36" y="46" width="22" height="6"/><rect x="36" y="58" width="22" height="6"/>
      <rect x="70" y="34" width="22" height="6"/><rect x="70" y="46" width="22" height="6"/><rect x="70" y="58" width="22" height="6"/>
    </g>
    <g font-size="1.7" font-weight="600"><text x="40" y="38">▸ PRIMARY</text><text x="40" y="50">▸ SECONDARY</text><text x="40" y="62">▸ THIRTIARY</text>
    <text x="74" y="38">▸ PRIMARY</text><text x="74" y="50">▸ SECONDARY</text><text x="74" y="62">▸ THIRTIARY</text></g>
    <path d="M18 33 Q10 55 18 76 M90 33 Q100 55 90 76" fill="none" stroke="var(--or)" stroke-width=".5"/>
    <rect x="9" y="76" width="16" height="6" fill="var(--or)"/><text x="17" y="79.5" fill="#fff" font-size="1.6" text-anchor="middle">BROKERAGE</text>
    <rect x="81" y="76" width="16" height="6" fill="var(--or)"/><text x="89" y="79.5" fill="#fff" font-size="1.6" text-anchor="middle">BROKERAGE</text>
  </svg>
  <div class="obox" style="left:122px;top:23px;width:38px;height:21px;padding:2px">
    <div style="font-size:2.2px;font-weight:600">Explanation One :</div>
    <div class="p">Tender loads to a ranked list of carriers in order of cost and fit.</div>
  </div>
  <div class="abs" style="left:122px;top:48px;width:38px">
    <div style="font-size:2.2px;font-weight:600">Explanation Two :</div>
    <div class="p">When all ranked carriers decline, the load falls back to the brokerage pool for cover.</div>
  </div>
</section>

<!-- Row 2 -->
<section class="slide dark">
  <div class="ph darkscene" role="img" aria-label="Truck on a road at dusk" style="inset:0"></div>
  <div class="abs brand" style="left:0;right:0;top:28px;text-align:center;font-size:6px">HAULWAY</div>
  <div class="abs" style="left:0;right:0;top:41px;text-align:center;font-size:5px;font-weight:600">Presentation Title Goes Here</div>
  <div class="abs" style="left:0;right:0;top:52px;text-align:center;font-size:3px;font-weight:600">Mr. Owen <span class="or">Marlow</span></div>
  <div class="abs" style="left:8px;bottom:6px;font-size:2px;color:#bbb">August 2024</div>
  <div class="abs or" style="right:8px;bottom:6px;font-size:2px">haulway.co</div>
</section>

<section class="slide dark">
  <div class="ph darkscene" role="img" aria-label="Trucks on a highway at dusk" style="inset:0"></div>
  <div class="abs brand" style="left:9px;top:26px;font-size:5.5px">HAULWAY</div>
  <div class="abs" style="left:9px;top:39px;font-size:5px;font-weight:600">Presentation Title Goes Here</div>
  <div class="abs" style="left:9px;top:47px;font-size:2.3px;color:#bbb">Presentation subtitle Goes Here</div>
  <div class="abs" style="left:9px;top:61px;font-size:3px;font-weight:600">Mr. Owen <span class="or">Marlow</span></div>
  <div class="abs" style="left:9px;bottom:6px;font-size:2px;color:#bbb">August 2024</div>
</section>

<section class="slide">
  <div class="abs brand" style="left:0;right:0;top:27px;text-align:center;font-size:6px">HAULWAY</div>
  <div class="abs" style="left:0;right:0;top:41px;text-align:center;font-size:5px;font-weight:600">Presentation Title Goes Here</div>
  <div class="abs" style="left:0;right:0;top:49px;text-align:center;font-size:2.3px;color:var(--mute)">Presentation subtitle Goes Here</div>
  <div class="abs" style="left:0;right:0;top:63px;text-align:center;font-size:3px;font-weight:600">Mr. Owen <span class="or">Marlow</span></div>
  <div class="abs" style="left:8px;bottom:6px;font-size:2px;color:var(--mute)">August 2024</div>
  <div class="abs or" style="right:8px;bottom:6px;font-size:2px">haulway.co</div>
</section>

<section class="slide">
  <div class="t" style="top:9px">Presentation List</div>
  <div class="abs p" style="left:0;right:0;top:16px;text-align:center;font-size:1.7px">Here Our Creative Subtitle</div>
  <div class="abs" style="left:22px;top:28px;width:50px;line-height:0">
    <div class="rowline" style="margin-bottom:8px"><span>COVER SLIDES</span><span>01</span></div>
    <div class="rowline or" style="margin-bottom:8px;border-color:var(--or);color:var(--or)"><span>PRESENTATION LIST</span><span>02</span></div>
    <div class="rowline" style="margin-bottom:8px"><span>ABOUT US</span><span>04</span></div>
    <div class="rowline"><span>OUR MISSIONS &amp; VISION</span><span>06</span></div>
  </div>
  <div class="abs" style="left:94px;top:28px;width:50px">
    <div class="rowline" style="margin-bottom:8px"><span>INFOGRAPH ONE</span><span>07</span></div>
    <div class="rowline" style="margin-bottom:8px"><span>INFOGRAPH TWO</span><span>08</span></div>
    <div class="rowline" style="margin-bottom:8px"><span>INFOGRAPH THREE</span><span>09</span></div>
    <div class="rowline"><span>CLOSING SLIDES</span><span>10</span></div>
  </div>
  <div class="foot"><span>haulway.co</span><span class="brand">HAULWAY</span><span>page 4</span></div>
</section>

<section class="slide">
  <div class="abs" style="left:12px;top:24px;width:8px;height:.6px;background:var(--or)"></div>
  <div class="abs" style="left:12px;top:28px;font-size:5.5px;line-height:1.5">Table Report<br>Brokerage Plan</div>
  <div class="abs p" style="left:12px;top:48px;width:50px">Short summary of rates per trailer length across two price ranges this quarter.</div>
  <div class="abs" style="left:84px;top:21px;width:66px">
    <div style="display:flex;background:var(--or);color:#fff;font-size:1.8px;padding:1px 2px"><span style="flex:1">FEET</span><span style="flex:1;text-align:center">Range I</span><span style="flex:1;text-align:right">Range II</span></div>
    <div class="rowline" style="padding:2px"><span style="flex:1">4 - 8 FEET</span><span style="flex:1;text-align:center">75.45</span><span style="flex:1;text-align:right">48.73</span></div>
    <div class="rowline" style="padding:2px;border-left:.6px solid var(--or)"><span style="flex:1">10 - 15 FEET</span><span style="flex:1;text-align:center">31.35</span><span style="flex:1;text-align:right">30.19</span></div>
    <div class="rowline" style="padding:2px"><span style="flex:1">15 - 20 FEET</span><span style="flex:1;text-align:center">19.58</span><span style="flex:1;text-align:right">18.54</span></div>
    <div class="rowline" style="padding:2px;border-left:.6px solid var(--or)"><span style="flex:1">20 - 25 FEET</span><span style="flex:1;text-align:center">13.25</span><span style="flex:1;text-align:right">12.43</span></div>
    <div class="rowline" style="padding:2px"><span style="flex:1">25+ FEET</span><span style="flex:1;text-align:center">5.78</span><span style="flex:1;text-align:right">5.48</span></div>
  </div>
  <div class="foot"><span>haulway.co</span><span class="brand">HAULWAY</span><span>page 5</span></div>
</section>

<section class="slide">
  <div class="ph road" role="img" aria-label="Yellow truck on an open road" style="left:18px;top:24px;width:44px;height:38px"></div>
  <div class="abs" style="left:84px;top:25px;width:8px;height:.6px;background:var(--or)"></div>
  <div class="abs" style="left:84px;top:29px;font-size:7px;line-height:1.5">Secure Shipping<br>with Us</div>
  <div class="abs p" style="left:84px;top:54px;width:60px">Reliable freight moves with tracking on every mile of the route.</div>
  <div class="foot"><span>haulway.co</span><span class="brand">HAULWAY</span><span>page 6</span></div>
</section>

<!-- Row 3 -->
<section class="slide">
  <div class="t" style="top:7px">Our Images</div>
  <div class="ph road" role="img" aria-label="Truck photo one" style="left:18px;top:18px;width:30px;height:17px"></div>
  <div class="ph road" role="img" aria-label="Truck photo two" style="left:68px;top:18px;width:30px;height:17px"></div>
  <div class="ph road" role="img" aria-label="Truck photo three" style="left:118px;top:18px;width:30px;height:17px"></div>
  <div class="ph night" role="img" aria-label="Truck photo four" style="left:18px;top:52px;width:30px;height:17px"></div>
  <div class="ph road" role="img" aria-label="Truck photo five" style="left:68px;top:52px;width:30px;height:17px"></div>
  <div class="ph night" role="img" aria-label="Truck photo six" style="left:118px;top:52px;width:30px;height:17px"></div>
  <div class="abs p" style="left:18px;top:37px;width:30px;text-align:center">Image One<br>Short caption text</div>
  <div class="abs p" style="left:68px;top:37px;width:30px;text-align:center">Image Two<br>Short caption text</div>
  <div class="abs p" style="left:118px;top:37px;width:30px;text-align:center">Image Three<br>Short caption text</div>
  <div class="abs p" style="left:18px;top:71px;width:30px;text-align:center">Image Four<br>Short caption text</div>
  <div class="abs p" style="left:68px;top:71px;width:30px;text-align:center">Image Five<br>Short caption text</div>
  <div class="abs p" style="left:118px;top:71px;width:30px;text-align:center">Image Six<br>Short caption text</div>
  <div class="foot"><span>haulway.co</span><span class="brand">HAULWAY</span><span>page 7</span></div>
</section>

<section class="slide">
  <div class="t" style="top:9px">Company Value</div>
  <div class="abs" style="left:14px;top:24px;width:140px;display:grid;grid-template-columns:repeat(3,1fr);gap:14px 6px;text-align:center">
    <div><div style="font-size:2.3px;font-weight:600">Value One</div><div class="p">Safe and on time delivery for every load we carry.</div></div>
    <div><div style="font-size:2.3px;font-weight:600">Value Two</div><div class="p">Clear pricing with no hidden fees at any stage.</div></div>
    <div><div style="font-size:2.3px;font-weight:600">Value Three</div><div class="p">Live tracking and fast answers from our team.</div></div>
    <div><div style="font-size:2.3px;font-weight:600">Value Four</div><div class="p">Trusted carrier network across every region.</div></div>
    <div><div style="font-size:2.3px;font-weight:600">Value Five</div><div class="p">Fair rates that stay steady through peak season.</div></div>
    <div><div style="font-size:2.3px;font-weight:600">Value Six</div><div class="p">Long term partners who grow with each shipper.</div></div>
  </div>
  <div class="foot"><span>haulway.co</span><span class="brand">HAULWAY</span><span>page 8</span></div>
</section>

<section class="slide">
  <div class="t" style="top:13px">Strategic <em>Partnerships</em></div>
  <div class="card" style="left:10px;top:34px;width:32px;height:33px;padding:2px"><div style="font-size:2px">Strategic Plan One</div><div class="p" style="margin-top:5px">1. Preparation<br>2. Meeting<br>3. Meeting Plan<br>4. Project Run</div></div>
  <div class="obox" style="left:46px;top:34px;width:32px;height:33px;padding:2px"><div style="font-size:2px">Strategic Plan Two</div><div class="p" style="margin-top:5px">1. Preparation<br>2. Meeting<br>3. Meeting Plan<br>4. Project Run</div></div>
  <div class="card" style="left:90px;top:34px;width:32px;height:33px;padding:2px"><div style="font-size:2px">Strategic Plan Three</div><div class="p" style="margin-top:5px">1. Preparation<br>2. Meeting<br>3. Meeting Plan<br>4. Project Run</div></div>
  <div class="card" style="left:126px;top:34px;width:32px;height:33px;padding:2px"><div style="font-size:2px">Strategic Plan Four</div><div class="p" style="margin-top:5px">1. Preparation<br>2. Meeting<br>3. Meeting Plan<br>4. Project Run</div></div>
  <div class="foot"><span>haulway.co</span><span class="brand">HAULWAY</span><span>page 9</span></div>
</section>

<section class="slide">
  <div class="t" style="top:10px">Brokerage Plan Business</div>
  <svg class="abs" viewBox="0 0 167 94" style="left:0;top:0;width:167px;height:94px">
    <line x1="50" y1="37" x2="73" y2="37" stroke="var(--or)" stroke-width=".5"/><line x1="93" y1="37" x2="116" y2="37" stroke="var(--or)" stroke-width=".5"/>
    <g fill="none" stroke="var(--or)" stroke-width=".6">
      <polygon points="40,27 49,32 49,42 40,47 31,42 31,32"/>
      <polygon points="83,27 92,32 92,42 83,47 74,42 74,32"/>
      <polygon points="126,27 135,32 135,42 126,47 117,42 117,32"/>
    </g>
    <g font-size="1.9" fill="var(--or)" text-anchor="middle"><text x="40" y="38">Step 1</text><text x="83" y="38">Step 2</text><text x="126" y="38">Step 3</text></g>
    <g font-size="1.7" fill="#888" text-anchor="middle"><text x="40" y="53">Short note on step one</text><text x="83" y="53">Short note on step two</text><text x="126" y="53">Short note on step three</text>
    <text x="83" y="67">Short summary of the plan and its main result</text></g>
    <text x="83" y="76" font-size="2" fill="var(--or)" font-weight="600" text-anchor="middle">$20,000 Lorem Ipsum</text>
  </svg>
  <div class="foot"><span>haulway.co</span><span class="brand">HAULWAY</span><span>page 10</span></div>
</section>

<section class="slide">
  <div class="t" style="top:10px">The Shipment Challenge</div>
  <div class="card" style="left:14px;top:28px;width:35px;height:40px;text-align:center;padding:3px"><div style="font-size:2px">Who?</div><div style="width:5px;height:5px;margin:5px auto;border:.6px solid var(--ink);border-radius:50%"></div><div class="p">Short note on who ships</div></div>
  <div class="card" style="left:66px;top:28px;width:35px;height:40px;text-align:center;padding:3px"><div style="font-size:2px">Where?</div><div style="width:5px;height:5px;margin:5px auto;border:.6px solid var(--ink);border-radius:50%"></div><div class="p">Short note on the route</div></div>
  <div class="card" style="left:118px;top:28px;width:35px;height:40px;text-align:center;padding:3px"><div style="font-size:2px">When?</div><div style="width:5px;height:5px;margin:5px auto;border:.6px solid var(--ink);border-radius:50%"></div><div class="p">Short note on the date</div></div>
  <div class="foot"><span>haulway.co</span><span class="brand">HAULWAY</span><span>page 11</span></div>
</section>

<section class="slide">
  <div class="t" style="top:10px">The Shipping Challenge</div>
  <div class="abs" style="left:0;right:0;top:24px;text-align:center;font-size:2.1px">Competition format</div>
  <div class="ph night" role="img" aria-label="Semi truck on a highway" style="left:23px;top:38px;width:48px;height:23px"></div>
  <div class="ph road" role="img" aria-label="Blue truck at sunset" style="left:96px;top:38px;width:48px;height:23px"></div>
  <div class="abs p" style="left:23px;top:64px;width:48px;text-align:center">Short caption for the first challenge</div>
  <div class="abs p" style="left:96px;top:64px;width:48px;text-align:center">Short caption for the second challenge</div>
  <div class="foot"><span>haulway.co</span><span class="brand">HAULWAY</span><span>page 12</span></div>
</section>

<!-- Row 4 -->
<section class="slide">
  <div class="abs" style="left:8px;top:6px;width:6px;height:.6px;background:var(--or)"></div>
  <div class="abs" style="left:8px;top:8px;font-size:5.2px">Timeline <span class="or">List</span></div>
  <svg class="abs" viewBox="0 0 167 94" style="left:0;top:0;width:167px;height:94px">
    <line x1="10" y1="46" x2="158" y2="46" stroke="#bbb" stroke-width=".4"/>
    <g fill="var(--or)"><circle cx="21" cy="46" r="3.5"/><circle cx="48" cy="46" r="3.5"/><circle cx="75" cy="46" r="3.5"/><circle cx="102" cy="46" r="3.5"/><circle cx="129" cy="46" r="3.5"/></g>
    <g stroke="#bbb" stroke-width=".3" stroke-dasharray="1 1"><line x1="48" y1="28" x2="48" y2="42"/><line x1="102" y1="28" x2="102" y2="42"/><line x1="21" y1="50" x2="21" y2="62"/><line x1="75" y1="50" x2="75" y2="62"/><line x1="129" y1="50" x2="129" y2="62"/></g>
    <g font-size="1.8" font-weight="600"><text x="47" y="26">Early Q2 2025</text><text x="101" y="26">Q3 2025</text><text x="21" y="61">Early Q1 2025</text><text x="75" y="61">Late Q2 2025</text><text x="129" y="61">October 2025</text></g>
    <g font-size="1.6" fill="#888"><text x="47" y="29">Short plan note here</text><text x="101" y="29">Short plan note here</text><text x="21" y="64">Short plan note here</text><text x="75" y="64">Short plan note here</text><text x="129" y="64">Short plan note here</text></g>
  </svg>
  <div class="foot"><span>haulway.co</span><span class="brand">HAULWAY</span><span>page 13</span></div>
</section>

<section class="slide">
  <div class="t" style="top:12px">Plan and Goal</div>
  <div class="card" style="left:25px;top:33px;width:50px;height:34px;padding:3px">
    <div class="or" style="text-align:center;font-size:2.3px;font-weight:600;margin-bottom:2px">What we'd like</div>
    <div class="p">• Grow regional lanes<br>• Add new carriers<br>• Cut empty miles<br>• Faster quotes<br>• Better tracking</div>
  </div>
  <div class="card" style="left:91px;top:33px;width:50px;height:34px;padding:3px">
    <div class="or" style="text-align:center;font-size:2.3px;font-weight:600;margin-bottom:2px">What you'll get</div>
    <div class="p">• Steady rates<br>• Live updates<br>• One contact desk<br>• Safe delivery<br>• Clear reports</div>
  </div>
  <div class="foot"><span>haulway.co</span><span class="brand">HAULWAY</span><span>page 14</span></div>
</section>

<section class="slide">
  <div class="t" style="top:11px">Our Vission</div>
  <div class="obox" style="left:21px;top:27px;width:125px;height:44px;display:flex;align-items:center;justify-content:center;text-align:center;padding:6px;font-size:3.1px;font-style:italic;line-height:1.6;box-shadow:0 2px 4px rgba(0,0,0,.2)">
    We move freight with care, clear pricing and steady partners so every shipper can plan ahead and grow with confidence on every road.
  </div>
  <div class="foot"><span>haulway.co</span><span class="brand">HAULWAY</span><span>page 15</span></div>
</section>

<section class="slide">
  <div class="t" style="top:13px">Our Details</div>
  <div class="abs p" style="left:0;right:0;top:20px;text-align:center;font-size:1.7px">Here Our Creative Subtitle</div>
  <div class="abs p" style="left:22px;top:34px;width:123px;text-align:center"><span class="or">Lorem ipsum</span> short paragraph about the company, our reach across regions, the number of branches and customers we serve and the partners who help us deliver.</div>
  <div class="abs" style="left:18px;top:59px;width:131px;display:flex;justify-content:space-between;text-align:center">
    <div><div style="font-size:4px">41</div><div class="p">Total Branch</div></div>
    <div><div style="font-size:4px">1290</div><div class="p">Satisfy Customer</div></div>
    <div><div style="font-size:4px">23</div><div class="p">Partnership</div></div>
    <div><div style="font-size:4px">14</div><div class="p">Certifications</div></div>
  </div>
  <div class="foot"><span>haulway.co</span><span class="brand">HAULWAY</span><span>page 16</span></div>
</section>

<section class="slide">
  <div class="t" style="top:9px">Analyse Chart</div>
  <div class="abs" style="left:15px;top:26px;font-size:1.9px">Circle Finding Chart</div>
  <svg class="abs" viewBox="0 0 167 94" style="left:0;top:0;width:167px;height:94px">
    <g font-size="1.6" fill="#555"><text x="24" y="38">Data Five</text><text x="24" y="44.5">Data Four</text><text x="24" y="51">Data Three</text><text x="24" y="57.5">Data Two</text><text x="24" y="64">Data One</text></g>
    <rect x="35" y="36.2" width="9" height="2.4" fill="var(--or)"/><rect x="35" y="42.7" width="10" height="2.4" fill="#777"/><rect x="35" y="49.2" width="5" height="2.4" fill="var(--or)"/><rect x="35" y="55.7" width="19" height="2.4" fill="#333"/><rect x="35" y="62.2" width="22" height="2.4" fill="var(--or)"/>
    <g font-size="1.5" fill="#888"><text x="35" y="69">0</text><text x="45" y="69">100</text><text x="56" y="69">200</text></g>
  </svg>
  <div class="card" style="left:75px;top:26px;width:78px;height:46px;padding:3px">
    <div style="font-size:1.8px;font-weight:600">• Analyse One:</div><div class="p">Short note on the first data set and what it shows about the lanes.</div>
    <div style="font-size:1.8px;font-weight:600;margin-top:2px">• Analyse Two:</div><div class="p">Short note on the second data set and the growth in volume.</div>
    <div style="font-size:1.8px;font-weight:600;margin-top:2px">• Analyse Three:</div><div class="p">Short note on the third data set and next steps.</div>
  </div>
  <div class="foot"><span>haulway.co</span><span class="brand">HAULWAY</span><span>page 17</span></div>
</section>

<section class="slide">
  <div class="ph road" role="img" aria-label="Yellow truck front view" style="left:5px;top:8px;width:34px;height:34px"></div>
  <div class="ph road" role="img" aria-label="Blue truck at sunset" style="left:73px;top:8px;width:34px;height:34px"></div>
  <div class="ph night" role="img" aria-label="Truck on a night road" style="left:39px;top:42px;width:34px;height:34px"></div>
  <div class="abs p" style="left:42px;top:18px;width:28px">Short caption for the first photo.</div>
  <div class="abs p" style="left:6px;top:53px;width:30px">Short caption for the second photo.</div>
  <div class="abs p" style="left:75px;top:53px;width:30px">Short caption for the third photo.</div>
  <div class="abs" style="left:115px;top:38px;font-size:5.5px">Gallery</div>
  <div class="abs p" style="left:115px;top:46px;width:44px">Short caption for the gallery section.</div>
  <div class="foot"><span>haulway.co</span><span class="brand">HAULWAY</span><span>page 18</span></div>
</section>

<!-- Row 5 -->
<section class="slide">
  <div class="t" style="top:10px;font-weight:600">Member <em>Team</em></div>
  <div class="abs" style="left:13px;top:24px;width:141px;display:grid;grid-template-columns:repeat(4,1fr);gap:3px">
    <div style="text-align:center"><div style="background:var(--or);height:12px;position:relative"><div class="ph face" role="img" aria-label="Portrait of team member" style="left:8px;top:3px;width:17px;height:17px"></div></div><div style="font-size:2px;font-weight:600;margin-top:11px">Lena <span class="or">Ortis</span></div><div class="p">Manager of Ops</div><div class="p" style="margin-top:2px">Short bio line<br>Short bio line</div></div>
    <div style="text-align:center"><div style="background:var(--or);height:12px;position:relative"><div class="ph face" role="img" aria-label="Portrait of team member" style="left:8px;top:3px;width:17px;height:17px"></div></div><div style="font-size:2px;font-weight:600;margin-top:11px">Mira <span class="or">Calde</span></div><div class="p">Manager of Sales</div><div class="p" style="margin-top:2px">Short bio line<br>Short bio line</div></div>
    <div style="text-align:center"><div style="background:var(--or);height:12px;position:relative"><div class="ph face" role="img" aria-label="Portrait of team member" style="left:8px;top:3px;width:17px;height:17px"></div></div><div style="font-size:2px;font-weight:600;margin-top:11px">Theo <span class="or">Brand</span></div><div class="p">Manager of Fleet</div><div class="p" style="margin-top:2px">Short bio line<br>Short bio line</div></div>
    <div style="text-align:center"><div style="background:var(--or);height:12px;position:relative"><div class="ph face" role="img" aria-label="Portrait of team member" style="left:8px;top:3px;width:17px;height:17px"></div></div><div style="font-size:2px;font-weight:600;margin-top:11px">Nora <span class="or">Vell</span></div><div class="p">Manager of Care</div><div class="p" style="margin-top:2px">Short bio line<br>Short bio line</div></div>
  </div>
  <div class="foot"><span>haulway.co</span><span class="brand">HAULWAY</span><span>page 19</span></div>
</section>

<section class="slide">
  <div class="t" style="top:10px;font-weight:600">Member <em>Team</em></div>
  <div class="obox" style="left:14px;top:20px;width:68px;height:23px"></div>
  <div class="ph face" role="img" aria-label="Portrait of team lead" style="left:17px;top:22px;width:19px;height:19px"></div>
  <div class="abs" style="left:44px;top:28px;font-size:2.8px;color:#fff">Rhea Solane</div>
  <div class="abs" style="left:44px;top:33px;font-size:1.9px;color:#fde">Marketing Manager</div>
  <div class="ph face" role="img" aria-label="Portrait of staff member" style="left:95px;top:23px;width:11px;height:11px"></div>
  <div class="ph face" role="img" aria-label="Portrait of staff member" style="left:131px;top:23px;width:11px;height:11px"></div>
  <div class="ph face" role="img" aria-label="Portrait of staff member" style="left:23px;top:52px;width:11px;height:11px"></div>
  <div class="ph face" role="img" aria-label="Portrait of staff member" style="left:59px;top:52px;width:11px;height:11px"></div>
  <div class="ph face" role="img" aria-label="Portrait of staff member" style="left:95px;top:52px;width:11px;height:11px"></div>
  <div class="ph face" role="img" aria-label="Portrait of staff member" style="left:131px;top:52px;width:11px;height:11px"></div>
  <div class="abs p" style="left:88px;top:36px;width:25px;text-align:center;color:#333">Ivo Kent<br><span style="color:#999">Staff</span></div>
  <div class="abs p" style="left:124px;top:36px;width:25px;text-align:center;color:#333">Ada Rue<br><span style="color:#999">Staff</span></div>
  <div class="abs p" style="left:16px;top:65px;width:25px;text-align:center;color:#333">Sam Holt<br><span style="color:#999">Staff</span></div>
  <div class="abs p" style="left:52px;top:65px;width:25px;text-align:center;color:#333">Eli Marsh<br><span style="color:#999">Staff</span></div>
  <div class="abs p" style="left:88px;top:65px;width:25px;text-align:center;color:#333">Kai Dunn<br><span style="color:#999">Staff</span></div>
  <div class="abs p" style="left:124px;top:65px;width:25px;text-align:center;color:#333">Zoe Pratt<br><span style="color:#999">Staff</span></div>
  <div class="foot"><span>haulway.co</span><span class="brand">HAULWAY</span><span>page 20</span></div>
</section>

<section class="slide">
  <div class="abs" style="left:10px;top:24px;width:6px;height:.6px;background:var(--or)"></div>
  <div class="abs" style="left:10px;top:26px;font-size:5px;font-weight:600;line-height:1.2">Circle Graph<br><span class="or" style="font-weight:400">Analyse</span></div>
  <div class="abs p" style="left:10px;top:40px;width:48px">Short note on the share of loads per month for this year.</div>
  <svg class="abs" viewBox="0 0 167 94" style="left:0;top:0;width:167px;height:94px">
    <circle cx="83" cy="46" r="13" fill="none" stroke="#f6b49c" stroke-width="3"/>
    <circle cx="83" cy="46" r="13" fill="none" stroke="var(--or)" stroke-width="3" stroke-dasharray="60 22" transform="rotate(-90 83 46)"/>
    <g font-size="1.5" fill="#888"><text x="67" y="69">● Jan ● Feb ● Mar ● Apr ● May ● Jun</text></g>
  </svg>
  <div class="card" style="left:120px;top:23px;width:36px;height:15px;padding:2px;box-shadow:none;border:.4px solid #ddd"><div class="p">June</div><div style="text-align:right;font-size:5px;color:#555">$2700</div></div>
  <div class="card" style="left:120px;top:45px;width:36px;height:15px;padding:2px;box-shadow:none;border:.4px solid var(--or)"><div class="p or">March</div><div class="or" style="text-align:right;font-size:5px">$3600</div></div>
  <div class="foot"><span>haulway.co</span><span class="brand">HAULWAY</span><span>page 21</span></div>
</section>

<section class="slide">
  <div class="t" style="top:11px;font-weight:600">Infograph</div>
  <svg class="abs" viewBox="0 0 167 94" style="left:0;top:0;width:167px;height:94px">
    <g>
      <rect x="21" y="26" width="12" height="23" rx="6" fill="#4a4a4a"/><rect x="21" y="37" width="12" height="12" rx="6" fill="var(--or)"/>
      <rect x="58" y="26" width="12" height="23" rx="6" fill="#4a4a4a"/><rect x="58" y="37" width="12" height="12" rx="6" fill="var(--or)"/>
      <rect x="95" y="26" width="12" height="23" rx="6" fill="#4a4a4a"/><rect x="95" y="37" width="12" height="12" rx="6" fill="var(--or)"/>
      <rect x="132" y="26" width="12" height="23" rx="6" fill="#4a4a4a"/><rect x="132" y="37" width="12" height="12" rx="6" fill="var(--or)"/>
    </g>
    <g font-size="1.6" fill="#fff" text-anchor="middle"><text x="27" y="35">One</text><text x="64" y="35">Two</text><text x="101" y="35">Three</text><text x="138" y="35">Four</text></g>
    <g font-size="1.5" fill="#888" text-anchor="middle"><text x="27" y="55">Short step note</text><text x="64" y="55">Short step note</text><text x="101" y="55">Short step note</text><text x="138" y="55">Short step note</text></g>
    <g fill="var(--or)"><circle cx="27" cy="67" r="3.5"/><circle cx="64" cy="67" r="3.5"/><circle cx="101" cy="67" r="3.5"/><circle cx="138" cy="67" r="3.5"/></g>
  </svg>
  <div class="foot"><span>haulway.co</span><span class="brand">HAULWAY</span><span>page 22</span></div>
</section>

<section class="slide dark">
  <div class="t" style="top:11px;font-weight:600">Infograph</div>
  <svg class="abs" viewBox="0 0 167 94" style="left:0;top:0;width:167px;height:94px">
    <g fill="#2e2e2e" stroke="var(--or)" stroke-width=".4">
      <rect x="14" y="33" width="33" height="43" rx="3"/><rect x="50" y="33" width="33" height="43" rx="3"/><rect x="86" y="33" width="33" height="43" rx="3"/><rect x="122" y="33" width="33" height="43" rx="3"/>
    </g>
    <g fill="#3a3a3a"><circle cx="30" cy="34" r="7.5"/><circle cx="66" cy="34" r="7.5"/><circle cx="102" cy="34" r="7.5"/><circle cx="138" cy="34" r="7.5"/></g>
    <g fill="var(--or)"><circle cx="30" cy="34" r="5.5"/><circle cx="66" cy="34" r="5.5"/><circle cx="102" cy="34" r="5.5"/><circle cx="138" cy="34" r="5.5"/></g>
    <g font-size="3" fill="#fff" font-weight="600" text-anchor="middle"><text x="30" y="35">450</text><text x="66" y="35">460</text><text x="102" y="35">480</text><text x="138" y="35">490</text></g>
    <g font-size="2" fill="#fff" font-weight="600"><text x="17" y="56">Step One</text><text x="53" y="56">Step Two</text><text x="89" y="56">Step Three</text><text x="125" y="56">Step Four</text></g>
    <g font-size="1.5" fill="#aaa"><text x="17" y="60">Short step note</text><text x="53" y="60">Short step note</text><text x="89" y="60">Short step note</text><text x="125" y="60">Short step note</text></g>
  </svg>
  <div class="foot"><span>haulway.co</span><span class="brand">HAULWAY</span><span>page 23</span></div>
</section>

<section class="slide">
  <div class="t" style="top:11px;font-weight:600">Date Plan List</div>
  <div class="card" style="left:20px;top:28px;width:36px;height:44px;text-align:center;padding:3px"><div style="width:4px;height:4px;margin:0 auto;background:var(--or);border-radius:50%"></div><div class="or" style="font-size:3px;font-weight:600;margin-top:2px">23<sup>rd</sup></div><div class="p">• Short plan item<br>• Short plan item<br>• Short plan item</div></div>
  <div class="card" style="left:65px;top:28px;width:36px;height:44px;text-align:center;padding:3px"><div style="width:4px;height:4px;margin:0 auto;background:var(--or);border-radius:50%"></div><div class="or" style="font-size:3px;font-weight:600;margin-top:2px">11<sup>st</sup></div><div class="p">• Short plan item<br>• Short plan item<br>• Short plan item</div></div>
  <div class="card" style="left:110px;top:28px;width:36px;height:44px;text-align:center;padding:3px"><div style="width:4px;height:4px;margin:0 auto;background:var(--or);border-radius:1px"></div><div class="or" style="font-size:3px;font-weight:600;margin-top:2px">3<sup>rd</sup></div><div class="p">• Short plan item<br>• Short plan item<br>• Short plan item</div></div>
  <div class="foot"><span>haulway.co</span><span class="brand">HAULWAY</span><span>page 24</span></div>
</section>

<!-- Row 6 -->
<section class="slide">
  <div class="t" style="top:11px;font-weight:600">Monthly <em>Graph</em></div>
  <svg class="abs" viewBox="0 0 167 94" style="left:0;top:0;width:167px;height:94px">
    <g stroke="#eee" stroke-width=".3"><line x1="14" y1="38" x2="106" y2="38"/><line x1="14" y1="47" x2="106" y2="47"/><line x1="14" y1="56" x2="106" y2="56"/><line x1="14" y1="65" x2="106" y2="65"/></g>
    <polyline points="20,44 38,35 54,49 70,43 88,49 104,46" fill="none" stroke="var(--or)" stroke-width=".6"/>
    <g fill="var(--or)"><circle cx="20" cy="44" r=".8"/><circle cx="38" cy="35" r=".8"/><circle cx="54" cy="49" r=".8"/><circle cx="70" cy="43" r=".8"/><circle cx="88" cy="49" r=".8"/><circle cx="104" cy="46" r=".8"/></g>
    <g font-size="1.5" fill="#888"><text x="18" y="72">JAN</text><text x="36" y="72">FEB</text><text x="52" y="72">MAR</text><text x="68" y="72">APR</text><text x="86" y="72">MAY</text><text x="102" y="72">JUN</text></g>
    <polygon points="115,22 119,24 119,29 115,31 111,29 111,24" fill="var(--or)"/><text x="115" y="27.5" fill="#fff" font-size="2" text-anchor="middle">49</text>
    <polygon points="115,48 119,50 119,55 115,57 111,55 111,50" fill="var(--or)"/><text x="115" y="53.5" fill="#fff" font-size="2" text-anchor="middle">56</text>
    <text x="111" y="36" font-size="3.5">May</text><text x="111" y="62" font-size="3.5">Jun</text>
    <g font-size="1.5" fill="#999"><text x="111" y="40">Short note about May volume</text><text x="111" y="42.5">and the main change seen</text><text x="111" y="66">Short note about June volume</text><text x="111" y="68.5">and the main change seen</text></g>
  </svg>
  <div class="foot"><span>haulway.co</span><span class="brand">HAULWAY</span><span>page 25</span></div>
</section>

<section class="slide">
  <div class="t" style="top:11px;font-weight:600">Three Point <em>Rate</em></div>
  <svg class="abs" viewBox="0 0 167 94" style="left:0;top:0;width:167px;height:94px">
    <polyline points="25,54 47,67 70,36" fill="none" stroke="var(--or)" stroke-width="2.5"/>
    <g fill="var(--or)" stroke="#f9c7b4" stroke-width="1.4"><circle cx="25" cy="54" r="5.5"/><circle cx="47" cy="67" r="5.5"/><circle cx="70" cy="36" r="5.5"/></g>
    <g font-size="3" fill="#fff" text-anchor="middle" font-weight="600"><text x="25" y="55">1</text><text x="47" y="68">2</text><text x="70" y="37">3</text></g>
    <g font-size="3" fill="#333" font-weight="600"><text x="93" y="29">56%</text><text x="93" y="44">76%</text><text x="93" y="60">89%</text></g>
    <g font-size="1.5" fill="#999"><text x="93" y="32">Short note about the first rate</text><text x="93" y="34.5">and what it covers</text>
    <text x="93" y="47">Short note about the second rate</text><text x="93" y="49.5">and what it covers</text>
    <text x="93" y="63">Short note about the third rate</text><text x="93" y="65.5">and what it covers</text></g>
    <g stroke="var(--or)" stroke-width=".4"><line x1="93" y1="26" x2="97" y2="26"/><line x1="93" y1="41" x2="97" y2="41"/><line x1="93" y1="57" x2="97" y2="57"/></g>
  </svg>
  <div class="foot"><span>haulway.co</span><span class="brand">HAULWAY</span><span>page 26</span></div>
</section>

<section class="slide dark">
  <div class="t" style="top:11px;font-weight:600">Table <em>Chart</em></div>
  <div class="abs" style="left:24px;top:24px;width:119px;font-size:1.6px">
    <div style="display:flex;background:var(--or);padding:1.2px 2px"><span style="flex:1.4">Data Name</span><span style="flex:1">Number</span><span style="flex:1">Profit Rate</span><span style="flex:.8">Option</span><span style="flex:.6">Rate</span><span style="flex:1">Performance</span></div>
    <div style="display:flex;padding:1.5px 2px;border-bottom:.3px solid #444"><span style="flex:1.4">Data One</span><span style="flex:1">5,647</span><span style="flex:1">20.45</span><span style="flex:.8">Yes</span><span style="flex:.6">72</span><span style="flex:1">3,094</span></div>
    <div style="display:flex;padding:1.5px 2px;border-bottom:.3px solid #444;background:#2c2c2c"><span style="flex:1.4">Data Two</span><span style="flex:1">6,3444</span><span style="flex:1">34.5</span><span style="flex:.8">Yes</span><span style="flex:.6">67</span><span style="flex:1">2,397</span></div>
    <div style="display:flex;padding:1.5px 2px;border-bottom:.3px solid #444"><span style="flex:1.4">Data Three</span><span style="flex:1">34,322</span><span style="flex:1">56.7</span><span style="flex:.8">No</span><span style="flex:.6">77</span><span style="flex:1">9,887</span></div>
    <div style="display:flex;padding:1.5px 2px;border-bottom:.3px solid #444;background:#2c2c2c"><span style="flex:1.4">Data Four</span><span style="flex:1">7,655</span><span style="flex:1">6.56</span><span style="flex:.8">No</span><span style="flex:.6">89</span><span style="flex:1">77,444</span></div>
    <div style="display:flex;padding:1.5px 2px;border-bottom:.3px solid #444"><span style="flex:1.4">Data Five</span><span style="flex:1">7,445</span><span style="flex:1">76.5</span><span style="flex:.8">Yes</span><span style="flex:.6">90</span><span style="flex:1">98.9</span></div>
    <div style="display:flex;padding:1.5px 2px;background:#2c2c2c"><span style="flex:1.4">Data Six</span><span style="flex:1">9,999</span><span style="flex:1">69</span><span style="flex:.8">No</span><span style="flex:.6">67</span><span style="flex:1">98.7</span></div>
  </div>
  <div class="foot"><span>haulway.co</span><span class="brand">HAULWAY</span><span>page 27</span></div>
</section>

<section class="slide">
  <div class="t" style="top:9px;font-weight:600">KPI <em>Dashboard</em></div>
  <div class="abs" style="left:14px;top:18px;width:140px;display:flex;justify-content:space-between;text-align:center">
    <div><div class="or" style="font-size:1.6px">Project Done</div><div style="font-size:3px">563</div></div>
    <div><div class="or" style="font-size:1.6px">Monthly Earning</div><div style="font-size:3px">$32,470</div></div>
    <div><div class="or" style="font-size:1.6px">Customer Acc</div><div style="font-size:3px">3,877</div></div>
    <div><div class="or" style="font-size:1.6px">Claim</div><div style="font-size:3px">0</div></div>
  </div>
  <svg class="abs" viewBox="0 0 167 94" style="left:0;top:0;width:167px;height:94px">
    <g font-size="1.5"><text x="12" y="34">5 Active Dashboard</text><text x="63" y="34">2 User Per Rate</text><text x="113" y="34">4 Live Profit and Net</text></g>
    <g fill="var(--or)"><rect x="30" y="42" width="6" height="1.8"/><rect x="30" y="47" width="8" height="1.8"/><rect x="30" y="52" width="11" height="1.8"/><rect x="30" y="57" width="16" height="1.8"/><rect x="30" y="62" width="18" height="1.8"/></g>
    <g font-size="1.4" fill="#555"><text x="20" y="43.5">Data Five</text><text x="20" y="48.5">Data Four</text><text x="20" y="53.5">Data Three</text><text x="20" y="58.5">Data Two</text><text x="20" y="63.5">Data One</text></g>
    <circle cx="83" cy="53" r="8" fill="none" stroke="#f7c3ae" stroke-width="3"/>
    <circle cx="83" cy="53" r="8" fill="none" stroke="var(--or)" stroke-width="3" stroke-dasharray="38 12" transform="rotate(-90 83 53)"/>
    <g font-size="1.8" fill="#333" text-anchor="middle"><text x="134" y="44">Net Profit &amp; Net sales</text><text x="134" y="55">Net profit</text></g>
    <text x="134" y="61" font-size="2.6" fill="var(--or)" text-anchor="middle">$44.587M</text>
    <text x="134" y="65" font-size="1.6" fill="#888" text-anchor="middle">Net sales = $15M</text>
  </svg>
  <div class="foot"><span>haulway.co</span><span class="brand">HAULWAY</span><span>page 28</span></div>
</section>

<section class="slide">
  <div class="t" style="top:9px;font-weight:600">KPI <em>Dashboard</em></div>
  <svg class="abs" viewBox="0 0 167 94" style="left:0;top:0;width:167px;height:94px">
    <text x="10" y="20" font-size="1.5">Data Statistics</text><text x="120" y="20" font-size="1.5">Customer Email</text>
    <g fill="var(--or)">
      <rect x="18" y="31" width="2" height="17"/><rect x="25" y="28" width="2" height="20"/><rect x="32" y="34" width="2" height="14"/><rect x="39" y="27" width="2" height="21"/><rect x="46" y="29" width="2" height="19"/><rect x="53" y="26" width="2" height="22"/><rect x="60" y="31" width="2" height="17"/><rect x="67" y="28" width="2" height="20"/><rect x="74" y="26" width="2" height="22"/><rect x="81" y="30" width="2" height="18"/><rect x="88" y="28" width="2" height="20"/><rect x="95" y="27" width="2" height="21"/><rect x="102" y="29" width="2" height="19"/><rect x="109" y="26" width="2" height="22"/>
    </g>
    <circle cx="133" cy="34" r="9" fill="none" stroke="#f7c3ae" stroke-width="1"/>
    <path d="M133 25 A9 9 0 1 1 124 34" fill="none" stroke="var(--or)" stroke-width="1"/>
    <circle cx="133" cy="34" r="6" fill="none" stroke="var(--or)" stroke-width=".5"/>
    <g font-size="1.7" text-anchor="middle"><text x="22" y="63">Sales</text><text x="65" y="63">Revenue</text><text x="103" y="63">Clients</text><text x="142" y="63">Trade</text></g>
    <g font-size="1.7" fill="#555" text-anchor="middle"><text x="22" y="66">$7,433</text><text x="65" y="66">$4,280</text><text x="103" y="66">$5,291</text><text x="142" y="66">$7,780</text></g>
    <g fill="#fbd4c4"><path d="M10 79 L14 74 L18 77 L22 72 L27 76 L32 73 L34 79Z"/><path d="M53 79 L57 75 L61 76 L65 72 L70 75 L75 73 L77 79Z"/><path d="M130 79 L134 74 L138 77 L142 72 L147 76 L152 73 L154 79Z"/></g>
    <path d="M91 79 L95 74 L99 77 L103 72 L108 76 L113 73 L115 79Z" fill="#cfe6f4"/>
  </svg>
  <div class="foot"><span>haulway.co</span><span class="brand">HAULWAY</span><span>page 29</span></div>
</section>

<section class="slide">
  <div class="t" style="top:9px;font-weight:600">KPI <em>Dashboard</em></div>
  <svg class="abs" viewBox="0 0 167 94" style="left:0;top:0;width:167px;height:94px">
    <text x="11" y="18" font-size="1.5">Net Profit Margin</text><text x="118" y="18" font-size="1.5">Rate Profitability Indicator</text>
    <polyline points="16,28 28,26 40,27 52,25 64,27 76,24 88,26 100,25 110,27" fill="none" stroke="var(--or)" stroke-width=".4"/>
    <polyline points="16,32 28,31 40,33 52,30 64,32 76,29 88,32 100,30 110,31" fill="none" stroke="#f9a88a" stroke-width=".4"/>
    <polyline points="16,36 28,35 40,36 52,34 64,36 76,34 88,35 100,36 110,35" fill="none" stroke="#aaa" stroke-width=".4"/>
    <g fill="var(--or)"><rect x="134" y="23" width="9" height="1.8"/><rect x="134" y="28" width="6" height="1.8"/><rect x="134" y="33" width="8" height="1.8"/><rect x="134" y="38" width="5" height="1.8"/></g>
    <text x="11" y="46" font-size="1.5">Past Year vs Target vs Actual</text>
    <g fill="var(--or)"><rect x="18" y="62" width="2" height="14"/><rect x="28" y="65" width="2" height="11"/><rect x="38" y="60" width="2" height="16"/><rect x="48" y="63" width="2" height="13"/><rect x="58" y="59" width="2" height="17"/><rect x="68" y="64" width="2" height="12"/><rect x="78" y="58" width="2" height="18"/><rect x="88" y="61" width="2" height="15"/><rect x="98" y="60" width="2" height="16"/><rect x="108" y="62" width="2" height="14"/></g>
    <g fill="#444"><rect x="21" y="68" width="1.6" height="8"/><rect x="31" y="70" width="1.6" height="6"/><rect x="41" y="67" width="1.6" height="9"/><rect x="51" y="69" width="1.6" height="7"/><rect x="61" y="66" width="1.6" height="10"/><rect x="71" y="69" width="1.6" height="7"/><rect x="81" y="67" width="1.6" height="9"/><rect x="91" y="68" width="1.6" height="8"/><rect x="101" y="66" width="1.6" height="10"/><rect x="111" y="69" width="1.6" height="7"/></g>
    <polyline points="16,60 30,58 44,55 58,57 72,53 86,55 100,52 112,54" fill="none" stroke="var(--or)" stroke-width=".4"/>
    <rect x="121" y="54" width="2.5" height="2.5" fill="var(--or)"/><text x="125" y="56.5" font-size="2.2">78,260.130</text>
    <g font-size="1.4" fill="#999"><text x="121" y="61">Short note on profit</text><text x="121" y="63.5">against the target</text></g>
  </svg>
  <div class="foot"><span>haulway.co</span><span class="brand">HAULWAY</span><span>page 30</span></div>
</section>

<!-- Row 7 -->
<section class="slide">
  <div class="t" style="top:11px;font-weight:600">KPI <em>Dashboard</em></div>
  <svg class="abs" viewBox="0 0 167 94" style="left:0;top:0;width:167px;height:94px">
    <g stroke="#e6e6e6" stroke-width=".3"><line x1="44" y1="22" x2="44" y2="74"/><line x1="56" y1="22" x2="56" y2="74"/><line x1="68" y1="22" x2="68" y2="74"/><line x1="80" y1="22" x2="80" y2="74"/><line x1="92" y1="22" x2="92" y2="74"/><line x1="104" y1="22" x2="104" y2="74"/><line x1="116" y1="22" x2="116" y2="74"/><line x1="128" y1="22" x2="128" y2="74"/><line x1="140" y1="22" x2="140" y2="74"/></g>
    <g font-size="1.4" fill="#888"><text x="42" y="22">May</text><text x="54" y="22">Jun</text><text x="66" y="22">Jul</text><text x="78" y="22">Aug</text><text x="90" y="22">Sep</text><text x="102" y="22">Oct</text><text x="114" y="22">Nov</text><text x="126" y="22">Dec</text><text x="138" y="22">Jan</text></g>
    <rect x="12" y="33" width="5" height="2.4" rx="1.2" fill="var(--or-d)"/><rect x="12" y="45" width="5" height="2.4" rx="1.2" fill="var(--or)"/><rect x="12" y="57" width="5" height="2.4" rx="1.2" fill="#66768a"/>
    <g font-size="1.5" fill="#888"><text x="19" y="35">Team One</text><text x="19" y="47">Team Two</text><text x="19" y="59">Team Three</text></g>
    <rect x="50" y="33" width="18" height="4" rx="2" fill="var(--or-d)"/><rect x="90" y="33" width="50" height="4" rx="2" fill="#66768a"/>
    <rect x="78" y="39" width="38" height="4" rx="2" fill="var(--or)"/>
    <rect x="62" y="45" width="22" height="4" rx="2" fill="#66768a"/><rect x="96" y="45" width="40" height="4" rx="2" fill="var(--or-d)"/>
    <rect x="50" y="57" width="50" height="4" rx="2" fill="var(--or-d)"/><rect x="120" y="57" width="18" height="4" rx="2" fill="var(--or)"/>
    <g fill="var(--or)"><rect x="44" y="71" width="1.5" height="1.5"/><rect x="56" y="71" width="1.5" height="1.5"/><rect x="68" y="71" width="1.5" height="1.5"/><rect x="80" y="71" width="1.5" height="1.5"/><rect x="92" y="71" width="1.5" height="1.5"/><rect x="104" y="71" width="1.5" height="1.5"/><rect x="116" y="71" width="1.5" height="1.5"/><rect x="128" y="71" width="1.5" height="1.5"/><rect x="140" y="71" width="1.5" height="1.5"/></g>
    <g font-size="1.4" fill="#888"><text x="42" y="76">2022</text><text x="66" y="76">2023</text><text x="90" y="76">2023</text><text x="114" y="76">2024</text><text x="138" y="76">2024</text></g>
  </svg>
  <div class="foot"><span>haulway.co</span><span class="brand">HAULWAY</span><span>page 31</span></div>
</section>

<section class="slide dark">
  <div class="abs brand" style="left:0;right:0;top:21px;text-align:center;font-size:4.5px">HAULWAY</div>
  <div class="abs" style="left:0;right:0;top:30px;text-align:center;font-size:9px;font-weight:500">Thank You</div>
  <div class="abs" style="left:63px;top:46px;width:41px;height:.5px;background:var(--or)"></div>
  <div class="abs p" style="left:45px;top:50px;width:77px;text-align:center;color:#bbb">Thank you for your time. We look forward to moving your freight together.</div>
  <div class="abs" style="left:70px;top:64px;width:27px;display:flex;justify-content:space-between">
    <span style="width:4px;height:4px;border:.5px solid #fff;border-radius:50%"></span><span style="width:4px;height:4px;border:.5px solid #fff;border-radius:50%"></span><span style="width:4px;height:4px;border:.5px solid #fff;border-radius:50%"></span>
  </div>
</section>

<section class="slide">
  <div class="icons" style="grid-template-columns:repeat(6,1fr);top:16px;left:14px;right:14px;gap:14px 0">
    <div class="ic o"></div><div class="ic o"></div><div class="ic o"></div><div class="ic o"></div><div class="ic o"></div><div class="ic o"></div>
    <div class="ic o"></div><div class="ic o"></div><div class="ic o"></div><div class="ic o"></div><div class="ic o"></div><div class="ic o"></div>
    <div class="ic o" style="background:var(--or)"></div><div class="ic o" style="background:var(--or)"></div><div class="ic o" style="background:var(--or)"></div><div class="ic o" style="background:var(--or)"></div><div class="ic o" style="background:var(--or)"></div><div class="ic o" style="background:var(--or)"></div>
  </div>
  <div class="foot"><span>haulway.co</span><span class="brand">HAULWAY</span><span>page</span></div>
</section>

<section class="slide">
  <div class="abs or" style="left:0;right:0;top:2px;text-align:center;font-size:1.9px">Business</div>
  <div class="icons" style="grid-template-columns:repeat(12,1fr);top:13px;left:10px;right:10px;gap:7px 0">
    <div class="ic"></div><div class="ic"></div><div class="ic"></div><div class="ic"></div><div class="ic"></div><div class="ic"></div><div class="ic"></div><div class="ic"></div><div class="ic"></div><div class="ic"></div><div class="ic"></div><div class="ic"></div>
    <div class="ic f"></div><div class="ic f"></div><div class="ic f"></div><div class="ic f"></div><div class="ic f"></div><div class="ic f"></div><div class="ic f"></div><div class="ic f"></div><div class="ic f"></div><div class="ic f"></div><div class="ic f"></div><div class="ic f"></div>
    <div class="ic"></div><div class="ic"></div><div class="ic"></div><div class="ic"></div><div class="ic"></div><div class="ic"></div><div class="ic"></div><div class="ic"></div><div class="ic"></div><div class="ic"></div><div class="ic"></div><div class="ic"></div>
    <div class="ic f"></div><div class="ic f"></div><div class="ic f"></div><div class="ic f"></div><div class="ic f"></div><div class="ic f"></div><div class="ic f"></div><div class="ic f"></div><div class="ic f"></div><div class="ic f"></div><div class="ic f"></div><div class="ic f"></div>
    <div class="ic"></div><div class="ic"></div><div class="ic"></div><div class="ic"></div><div class="ic"></div><div class="ic"></div><div class="ic"></div><div class="ic"></div><div class="ic"></div><div class="ic"></div><div class="ic"></div><div class="ic"></div>
    <div class="ic f"></div><div class="ic f"></div><div class="ic f"></div><div class="ic f"></div><div class="ic f"></div><div class="ic f"></div><div class="ic f"></div><div class="ic f"></div><div class="ic f"></div><div class="ic f"></div><div class="ic f"></div><div class="ic f"></div>
  </div>
  <div class="foot"><span>haulway.co</span><span class="brand">HAULWAY</span><span>page</span></div>
</section>

<section class="slide">
  <div class="abs or" style="left:0;right:0;top:2px;text-align:center;font-size:1.9px">Business</div>
  <div class="icons" style="grid-template-columns:repeat(12,1fr);top:13px;left:10px;right:10px;gap:7px 0">
    <div class="ic"></div><div class="ic"></div><div class="ic"></div><div class="ic"></div><div class="ic"></div><div class="ic"></div><div class="ic"></div><div class="ic"></div><div class="ic"></div><div class="ic"></div><div class="ic"></div><div class="ic"></div>
    <div class="ic f"></div><div class="ic f"></div><div class="ic f"></div><div class="ic f"></div><div class="ic f"></div><div class="ic f"></div><div class="ic f"></div><div class="ic f"></div><div class="ic f"></div><div class="ic f"></div><div class="ic f"></div><div class="ic f"></div>
    <div class="ic"></div><div class="ic"></div><div class="ic"></div><div class="ic"></div><div class="ic" style="border-color:#eee;background:#f2f2f2"></div><div class="ic" style="border-color:#eee;background:#f2f2f2"></div><div class="ic" style="border-color:#eee;background:#f2f2f2"></div><div class="ic" style="border-color:#eee;background:#f2f2f2"></div><div class="ic" style="border-color:#eee;background:#f2f2f2"></div><div class="ic" style="border-color:#eee;background:#f2f2f2"></div><div class="ic" style="border-color:#eee;background:#f2f2f2"></div><div class="ic" style="border-color:#eee;background:#f2f2f2"></div>
    <div class="ic f"></div><div class="ic f"></div><div class="ic f"></div><div class="ic f"></div><div class="ic" style="border-color:#eee;background:#f2f2f2"></div><div class="ic" style="border-color:#eee;background:#f2f2f2"></div><div class="ic" style="border-color:#eee;background:#f2f2f2"></div><div class="ic" style="border-color:#eee;background:#f2f2f2"></div><div class="ic" style="border-color:#eee;background:#f2f2f2"></div><div class="ic" style="border-color:#eee;background:#f2f2f2"></div><div class="ic" style="border-color:#eee;background:#f2f2f2"></div><div class="ic" style="border-color:#eee;background:#f2f2f2"></div>
  </div>
  <div class="foot"><span>haulway.co</span><span class="brand">HAULWAY</span><span>page</span></div>
</section>

<section class="slide">
  <div class="abs or" style="left:0;right:0;top:2px;text-align:center;font-size:1.9px">Communication</div>
  <div class="icons" style="grid-template-columns:repeat(12,1fr);top:13px;left:10px;right:10px;gap:7px 0">
    <div class="ic"></div><div class="ic"></div><div class="ic"></div><div class="ic"></div><div class="ic"></div><div class="ic"></div><div class="ic"></div><div class="ic"></div><div class="ic"></div><div class="ic"></div><div class="ic"></div><div class="ic"></div>
    <div class="ic f"></div><div class="ic f"></div><div class="ic f"></div><div class="ic f"></div><div class="ic f"></div><div class="ic f"></div><div class="ic f"></div><div class="ic f"></div><div class="ic f"></div><div class="ic f"></div><div class="ic f"></div><div class="ic f"></div>
    <div class="ic"></div><div class="ic"></div><div class="ic"></div><div class="ic"></div><div class="ic"></div><div class="ic"></div><div class="ic"></div><div class="ic"></div><div class="ic"></div><div class="ic"></div><div class="ic" style="border-color:#eee;background:#f2f2f2"></div><div class="ic" style="border-color:#eee;background:#f2f2f2"></div>
    <div class="ic f"></div><div class="ic f"></div><div class="ic f"></div><div class="ic f"></div><div class="ic f"></div><div class="ic f"></div><div class="ic f"></div><div class="ic f"></div><div class="ic f"></div><div class="ic f"></div><div class="ic" style="border-color:#eee;background:#f2f2f2"></div><div class="ic" style="border-color:#eee;background:#f2f2f2"></div>
  </div>
  <div class="foot"><span>haulway.co</span><span class="brand">HAULWAY</span><span>page</span></div>
</section>

</main>
</body>
</html>
```